Corrow Family Farm fresh honey jar label

I need a label for jars of honey harvested at our farm. These are for gifts and personal use. We are looking to incorporate our farm brand into the label. We would like the design to take the existing brand and add some element like bees, honey, flowers, or hives to indicate the contents. We want the design to feel homemade and authentic without feeling cheap or hoaky

Requirements
Must have
• The label must be made to fit a 1" x2" rectangular label. The label must include the attached family brand. The label must include the text "Corrow Family Farms" "Pinebrook, USA" "Farm Fresh Honey". The label will be printed on off-white paper
Nice to have
• It would be nice to have illustrations of bees or flowers around the logo or hives or honeycombs. The label should have a vintage feel
Should not have
• The label should not feel overly cartoonish or hoaky

```html
<!DOCTYPE html>
<html lang="en">
<head>
<meta charset="utf-8">
<title>Corrow Family Farm – Farm Fresh Honey Label</title>
<link rel="stylesheet" href="https://fonts.googleapis.com/css2?family=Cormorant+Garamond:wght@600&family=Montserrat:wght@500&display=swap">
<style>
  :root {
    --page: #ffffff;
    --label: #c0e3dc;
    --glow: #d6eeea;
    --brown: #4b2812;
    --accent-bar: #a8ece2;
    --petal: #ef7a63;
    --leaf: #a9d6b8;
    --bee: #efc94c;
  }
  * { margin: 0; padding: 0; box-sizing: border-box; }
  html, body {
    width: 1200px; height: 1200px; overflow: hidden;
    background: var(--page);
  }
  .label {
    position: absolute; left: 330px; top: 60px;
    width: 540px; height: 1080px;
    background: var(--label);
    color: var(--brown);
  }
  .rule {
    position: absolute; left: 0; width: 100%;
    background: var(--brown);
  }
  .rule--top-thick { top: 35px; height: 7px; }
  .rule--top-thin { top: 48px; height: 5px; }
  .rule--bottom-thin { top: 1027px; height: 5px; }
  .rule--bottom-thick { top: 1037px; height: 7px; }
  .title {
    position: absolute; left: 0; width: 100%;
    text-align: center;
    font-family: "Cormorant Garamond", serif;
    font-weight: 600;
    line-height: 1;
  }
  .title__kicker { top: 132px; font-size: 64px; letter-spacing: 1px; }
  .title__main { top: 198px; font-size: 108px; letter-spacing: 2px; }
  .glow {
    position: absolute; left: 87px; top: 357px;
    width: 366px; height: 366px; border-radius: 50%;
    background: radial-gradient(circle, var(--glow) 40%, rgba(214,238,234,0) 72%);
  }
  .artwork {
    position: absolute; left: 121px; top: 393px;
    width: 330px; height: 322px;
  }
  .farm-name, .farm-place, .farm-mark {
    position: absolute; left: 0; width: 100%;
    text-align: center;
    font-family: "Montserrat", sans-serif;
    font-weight: 500;
    line-height: 1;
  }
  .farm-name { top: 768px; font-size: 43px; }
  .farm-place { top: 823px; font-size: 24px; letter-spacing: 0.3px; }
  .farm-mark { top: 905px; font-size: 34px; letter-spacing: 2px; }
  .accent-bar {
    position: absolute; left: 432px; top: 972px;
    width: 108px; height: 6px;
    background: var(--accent-bar);
  }
</style>
</head>
<body>
  <div class="label">
    <div class="rule rule--top-thick"></div>
    <div class="rule rule--top-thin"></div>

    <div class="title title__kicker">FARM FRESH</div>
    <div class="title title__main">HONEY</div>

    <div class="glow"></div>
    <svg class="artwork" viewBox="0 0 330 322" role="img" aria-label="Watercolour illustration of a honeybee flying above a cluster of coral and orange flowers with leaves">
      <defs>
        <radialGradient id="flowers" cx="45%" cy="60%" r="55%">
          <stop offset="0%" stop-color="#f08a6e"/>
          <stop offset="60%" stop-color="#f3a27e" stop-opacity="0.8"/>
          <stop offset="100%" stop-color="#f3a27e" stop-opacity="0"/>
        </radialGradient>
        <radialGradient id="bee" cx="50%" cy="50%" r="50%">
          <stop offset="0%" stop-color="#efc94c"/>
          <stop offset="100%" stop-color="#efc94c" stop-opacity="0"/>
        </radialGradient>
      </defs>
      <ellipse cx="130" cy="225" rx="130" ry="100" fill="url(#flowers)"/>
      <ellipse cx="240" cy="75" rx="70" ry="55" fill="url(#bee)"/>
    </svg>

    <div class="farm-name">Corrow Family Farm</div>
    <div class="farm-place">Pinebrook, Louisiana – USA</div>
    <div class="farm-mark">CORROW</div>

    <div class="accent-bar"></div>

    <div class="rule rule--bottom-thin"></div>
    <div class="rule rule--bottom-thick"></div>
  </div>
</body>
</html>
```